Maple Crest

We have opened new business that includes pottery & chimineas we want cards to have collage of pictures of products on front of card then information on back. On back in middle MAPLE CREST +
marla_fenwick@quillmail.net
(555) 218-0347
(555)2180392 & maplecrest@quillmail.net
Industry/Entity Type
Business
Font styles to use
Sans Serif
Decorative

```html
<!DOCTYPE html>
<html lang="en">
<head>
<meta charset="utf-8">
<title>Maple Crest + Business Card</title>
<link href="https://fonts.googleapis.com/css2?family=Noto+Sans:wght@400;700;800&display=swap" rel="stylesheet">
<style>
  :root {
    --ink: #0d0d0d;
    --white: #ffffff;
    --paper-light: #f7f7f7;
    --paper-mid: #e4e4e4;
    --glaze-teal: #3f8a86;
    --clay-rust: #7a4a32;
    --iron-dark: #2c2a24;
    --sand: #c9b37a;
    --frost: rgba(255, 255, 255, 0.28);
  }
  * { margin: 0; padding: 0; box-sizing: border-box; }
  html, body {
    width: 999px;
    height: 1200px;
    overflow: hidden;
    background: var(--white);
  }
  .card {
    position: relative;
    width: 999px;
    height: 1200px;
    overflow: hidden;
    font-family: "Noto Sans", sans-serif;
    color: var(--ink);
  }
  .product-collage {
    position: absolute;
    left: 0; top: 0;
    width: 999px; height: 599px;
    background:
      radial-gradient(ellipse at 12% 55%, var(--glaze-teal) 0%, transparent 45%),
      radial-gradient(ellipse at 30% 60%, var(--sand) 0%, transparent 40%),
      radial-gradient(ellipse at 55% 50%, var(--clay-rust) 0%, transparent 45%),
      radial-gradient(ellipse at 85% 30%, var(--iron-dark) 0%, transparent 45%),
      radial-gradient(ellipse at 88% 80%, #5f6e52 0%, transparent 40%),
      linear-gradient(135deg, #5c6b4a 0%, #7d6a3e 45%, #4b3a2c 75%, #3a3a30 100%);
  }
  .brand-title {
    position: absolute;
    left: 31px; top: 13px;
    width: 562px; height: 122px;
    background: var(--frost);
    border-radius: 14px;
    color: var(--white);
    font-weight: 700;
    font-size: 80px;
    line-height: 122px;
    padding-left: 20px;
    letter-spacing: -1px;
    white-space: nowrap;
  }
  .brand-tag {
    position: absolute;
    left: 666px; top: 373px;
    width: 149px; height: 167px;
    background: var(--frost);
    border-radius: 14px;
    display: flex;
    align-items: center;
    justify-content: center;
    text-align: center;
    color: var(--white);
    font-weight: 700;
    font-size: 30px;
    line-height: 1.15;
  }
  .backdrop {
    position: absolute;
    left: 0; top: 599px;
    width: 999px; height: 601px;
    background: linear-gradient(180deg, var(--paper-light) 0%, var(--paper-mid) 60%, var(--paper-light) 100%);
  }
  .business-name {
    position: absolute;
    left: 71px; top: 664px;
    font-weight: 800;
    font-size: 74px;
    line-height: 1;
    white-space: nowrap;
  }
  .owners {
    position: absolute;
    left: 73px; top: 757px;
    font-weight: 700;
    font-size: 36px;
    line-height: 1;
  }
  .label {
    position: absolute;
    left: 44px;
    font-size: 27px;
    line-height: 1;
  }
  .label.email-label { top: 938px; }
  .label.phone-label { top: 1095px; }
  .contact-line {
    position: absolute;
    font-size: 28px;
    line-height: 1;
    white-space: nowrap;
  }
  .email-primary { left: 118px; top: 986px; }
  .email-secondary { left: 118px; top: 1029px; }
  .phone-primary { left: 115px; top: 1146px; }
  .phone-secondary { left: 399px; top: 1146px; }
</style>
</head>
<body>
  <div class="card">
    <div class="product-collage" role="img" aria-label="Collage of photographs of glazed pottery, urns and chimineas"></div>
    <div class="brand-title">Maple Crest+</div>
    <div class="brand-tag">Maple<br>Crest</div>

    <div class="backdrop" role="img" aria-label="Faded photograph of decorative wrought iron scrollwork"></div>

    <h1 class="business-name">MAPLE CREST +</h1>
    <p class="owners">Dale &amp; Marla Fenwick</p>

    <p class="label email-label">Email:</p>
    <p class="contact-line email-primary">marla_fenwick@quillmail.net</p>
    <p class="contact-line email-secondary">maplecrest@quillmail.net</p>

    <p class="label phone-label">Phone:</p>
    <p class="contact-line phone-primary">(555) 218-0347</p>
    <p class="contact-line phone-secondary">(555) 218-0392</p>
  </div>
</body>
</html>
```